Keystone Lending and Capital. We provide MOSTLY residential home mortgages in Florida AND commercial loans for investment properties throughout the United states.
I would love to emulate so of the lender sites that are available on the internet but I would like to have the site as popular as possible for SEO purposes. Clients can already click the link to take them to the mortgage application where they can complete that and upload documents. If you could polish that up for me that would be great. I can also provide you with great detail on loan programs that are currently being offered. WE OFFER ALL MORTGAGE LENDING PRODUCTS. I would also like to add something in reference to the rate but I don't think it's legal to actually state or promise a rate for mortgage since they vary based on loan type, client and other criteria...

On the Keystone real estate site I would like to add a link or some way for clients to be able to put in credit card information to render services ...

Please let me know what you need from me

Thank you !!

Current link to site to improve and code

https://keystonelendingandcapital.example/

Residential and commmercial lending

Requirements
Must have
• Love to integrate Mortgage interest rates even if general
Nice to have
• Link to fill out mortgage application via Vanta LOS software

```html
<!DOCTYPE html>
<html lang="en">
<head>
<meta charset="utf-8">
<title>Keystone Lending and Capital</title>
<link rel="stylesheet" href="https://fonts.googleapis.com/css2?family=Outfit:wght@300;400;500;600;700;800&family=Lora:wght@500&display=swap">
<style>
:root{
  --green-dark:#1f3d17;
  --green:#8db93c;
  --green-soft:#eef3dc;
  --cream:#f7f7ec;
  --ink:#2a2a2a;
  --muted:#555;
  --line:#dcdcdc;
  --footer:#1c3a1c;
  --white:#fff;
  --gold:#f2b705;
  --chart:#f08a4b;
}
*{box-sizing:border-box;margin:0;padding:0}
html,body{width:1200px;height:4835px;overflow:hidden}
body{position:relative;font-family:'Outfit',sans-serif;color:var(--ink);background:var(--white)}
.section{position:absolute;left:0;width:1200px}
.abs{position:absolute}
.center{text-align:center}
.btn{position:absolute;display:flex;align-items:center;justify-content:center;gap:6px;border-radius:22px;font-size:12px;font-weight:500;text-decoration:none}
.btn-solid{background:var(--green);color:var(--green-dark)}
.btn-outline{border:1px solid #9a9a9a;color:var(--ink);background:#fff}
.heading{font-size:36px;font-weight:300;color:var(--green-dark);letter-spacing:.5px}
.heading b{font-weight:800}
.ph{background:linear-gradient(135deg,#8a9aa6,#4d5a4a)}

/* header */
.site-header{top:0;height:100px}
.brand{left:141px;top:24px;display:flex;align-items:center;gap:12px}
.brand-mark{width:52px;height:52px;border-radius:50%;background:var(--green-dark)}
.brand-name{font-size:10px;font-weight:700;color:var(--green-dark);letter-spacing:.4px;text-transform:uppercase}
.nav{right:143px;top:34px;display:flex;align-items:center;gap:28px;font-size:13px;color:var(--green-dark)}
.nav .contact{background:var(--green);padding:9px 20px;border-radius:3px;color:var(--green-dark)}

/* hero */
.hero{top:100px;height:529px}
.hero-photo{position:absolute;inset:0;background:linear-gradient(180deg,#9fb0a6 0%,#6f7c6c 45%,#2c2b22 100%)}
.hero-title{top:326px;width:100%;font-size:32px;font-weight:800;color:#fff;line-height:38px;text-transform:uppercase}
.hero-sub{top:410px;width:100%;font-size:16px;color:#fff}
.hero .btn{left:528px;top:456px;width:142px;height:38px;border-radius:3px}

/* stats */
.stats{top:633px;height:113px;background:var(--green-soft)}
.stat{position:absolute;top:32px;width:220px;margin-left:-110px;text-align:center}
.stat-num{font-family:'Lora',serif;font-size:27px;color:var(--ink)}
.stat-label{font-size:12px;margin-top:8px;text-transform:uppercase;color:var(--ink)}

/* properties */
.properties{top:746px;height:544px}
.underline{position:absolute;height:4px;background:var(--green)}
.prop-card{position:absolute;top:142px;width:212px;height:295px;border:1px solid #e4e4e4;border-radius:10px;background:#fff;box-shadow:0 2px 8px rgba(0,0,0,.06);text-align:center}
.prop-photo{position:absolute;left:8px;top:7px;right:8px;height:224px;border-radius:6px}
.prop-count{position:absolute;top:247px;width:100%;font-size:12px;color:var(--green);text-transform:uppercase}
.prop-name{position:absolute;top:262px;width:100%;font-size:16px;font-weight:500;color:var(--ink)}
.arrow-btn{position:absolute;top:270px;width:38px;height:38px;border-radius:50%;display:flex;align-items:center;justify-content:center}

/* about */
.about{top:1290px;height:556px}
.about-photo{left:126px;top:57px;width:404px;height:415px;border-radius:90px 0 6px 6px;background:linear-gradient(180deg,#9ec4e6 0%,#c9c3b6 55%,#3f4a3a 100%)}
.badge{left:451px;top:147px;width:137px;height:125px;background:var(--green);border:5px solid #fff;border-radius:60px 0 0 0;color:#fff;text-align:center;padding-top:18px}
.badge-num{font-size:50px;font-weight:600;line-height:52px}
.badge-label{font-size:10px;font-weight:500;color:var(--green-dark)}
.eyebrow{left:639px;top:56px;font-family:'Lora',serif;font-size:18px;color:var(--green)}
.about-title{left:639px;top:84px;font-size:36px;line-height:45px;font-weight:300;color:var(--green-dark)}
.about-title b{font-weight:800}
.about-text{left:639px;top:194px;width:420px;font-size:13.3px;line-height:25.5px;color:var(--ink)}
.call{left:789px;top:417px;display:flex;align-items:center;gap:10px}
.call-icon{width:44px;height:44px;border-radius:50%;background:var(--green-dark);display:flex;align-items:center;justify-content:center}
.call small{display:block;font-size:9px;font-weight:600;color:var(--green-dark)}
.call strong{font-size:12px;color:var(--green-dark)}

/* services */
.services{top:1846px;height:574px}
.services-photo{position:absolute;left:0;top:0;width:1200px;height:413px;background:linear-gradient(180deg,#6f9ccd 0%,#9dbbd8 45%,#6f8aa0 70%,#3f5c78 100%)}
.services .heading{color:#fff}
.service-card{position:absolute;top:282px;width:290px;height:261px;background:#fff;border-radius:10px;box-shadow:0 4px 14px rgba(0,0,0,.08);text-align:center}
.service-icon{position:absolute;left:103px;top:-41px;width:84px;height:84px;background:var(--green);border-radius:12px 12px 40px 40px;border:4px solid #fff;display:flex;align-items:center;justify-content:center}
.service-title{position:absolute;top:76px;width:100%;font-size:20px;font-weight:600;color:var(--green-dark);text-transform:uppercase}
.service-text{position:absolute;top:100px;left:20px;right:20px;font-size:13px;line-height:25px;color:var(--ink)}
.service-card .btn{left:77px;top:191px;width:135px;height:38px}

/* rates */
.rates{top:2420px;height:857px}
.rates-text{top:175px;left:300px;width:600px;font-size:13.3px;line-height:25px;color:var(--ink)}
.chart-card{left:329px;top:279px;width:542px;height:413px;border:1px solid #e6e6e6;border-radius:10px;background:#fff;box-shadow:0 2px 10px rgba(0,0,0,.06)}
.chart-title{position:absolute;left:8px;top:10px;font-size:16px;font-weight:700;color:#222}
.chart-sub{position:absolute;left:8px;top:34px;width:500px;font-size:10px;line-height:13px;color:#333}
.chart-card svg{position:absolute;left:0;top:0}

/* testimonials */
.testimonials{top:3277px;height:586px;background:var(--cream)}
.t-card{position:absolute;top:165px;width:436px;height:269px;background:#fff;border-radius:8px;box-shadow:0 2px 10px rgba(0,0,0,.04);overflow:hidden}
.avatar{position:absolute;left:26px;top:23px;width:58px;height:65px;border-radius:6px;background:linear-gradient(180deg,#b7b0a6,#6c6258)}
.t-name{position:absolute;left:100px;top:38px;font-size:15px;font-weight:600;color:#111}
.stars{position:absolute;left:100px;top:57px;font-size:13px;letter-spacing:2px;color:var(--gold)}
.quote{position:absolute;right:22px;top:18px;font-size:90px;line-height:90px;font-weight:800;color:var(--green);font-family:Georgia,serif}
.t-text{position:absolute;left:26px;top:128px;right:22px;font-size:13px;line-height:25px;color:#333}
.dots{position:absolute;top:484px;left:535px;display:flex;gap:16px;align-items:center}
.dots i{display:block;width:6px;height:6px;border-radius:50%;background:#999}
.dots i.on{width:14px;height:14px;background:none;border:1.5px solid var(--green);position:relative}
.dots i.on::after{content:"";position:absolute;left:3px;top:3px;width:5px;height:5px;border-radius:50%;background:var(--green)}

/* contact */
.contact{top:3863px;height:601px}
.contact-sub{top:138px;width:100%;font-size:13px;color:var(--ink)}
.field{position:absolute;border:1px solid var(--line);border-radius:3px;background:#fff;display:flex;align-items:flex-start;gap:10px;padding:18px 14px;font-size:11px;color:#888}
.field .sep{width:1px;height:14px;background:var(--line)}
.send{left:291px;top:462px;width:618px;height:53px;background:var(--green);color:var(--green-dark);font-size:13px;font-weight:600;display:flex;align-items:center;justify-content:center;text-transform:uppercase;border-radius:2px}

/* footer */
.site-footer{top:4464px;height:371px;background:var(--footer);color:#fff}
.footer-brand{left:141px;top:80px;display:flex;align-items:center;gap:10px}
.footer-brand .brand-mark{width:38px;height:38px;background:#fff}
.footer-brand .brand-name{color:#fff;font-size:8px}
.footer-note{left:141px;top:140px;width:290px;font-size:12px;line-height:21px}
.newsletter{left:141px;top:197px;width:260px;height:32px;background:#fff;border-radius:16px;display:flex;align-items:center;padding-left:14px;gap:8px;font-size:11px;color:#999}
.newsletter .go{position:absolute;right:3px;top:3px;width:26px;height:26px;border-radius:50%;background:var(--green);display:flex;align-items:center;justify-content:center}
.f-head{font-size:18px;font-weight:500}
.f-list{list-style:none;font-size:13px}
.f-list li{height:28px}
.detail{position:absolute;left:635px;font-size:12px;line-height:20px}
.detail svg{position:absolute;left:0;top:3px}
.detail span{display:block;padding-left:21px}
.social{position:absolute;left:939px;display:flex;align-items:center;gap:10px;font-size:13px}
.social i{width:28px;height:28px;border-radius:50%;border:1px solid #fff;display:block}
.social i.on{background:var(--green);border-color:var(--green)}
.f-rule{left:0;top:316px;width:1200px;height:1px;background:rgba(255,255,255,.15)}
.copyright{top:341px;width:100%;font-size:12px}
</style>
</head>
<body>

<header class="section site-header">
  <div class="abs brand"><span class="brand-mark"></span><span class="brand-name">Keystone Lending and Capital of Florida</span></div>
  <nav class="abs nav">
    <span>Home</span><span>About Us</span><span>Properties</span><span class="contact">Contact Us</span>
  </nav>
</header>

<section class="section hero">
  <div class="hero-photo" role="img" aria-label="Smiling family standing in front of a modern home"></div>
  <h1 class="abs hero-title center">Unlock Your Future With Our<br>Tailored Mortgage Solutions</h1>
  <p class="abs hero-sub center">Residential and Commercial Mortgages across Florida and the USA</p>
  <a class="btn btn-solid">Get Started Now</a>
</section>

<section class="section stats">
  <div class="stat" style="left:225px"><div class="stat-num">850+</div><div class="stat-label">Elegant Apartments</div></div>
  <div class="stat" style="left:488px"><div class="stat-num">950+</div><div class="stat-label">Luxury Houses</div></div>
  <div class="stat" style="left:734px"><div class="stat-num">18k+</div><div class="stat-label">Satisfied Guests</div></div>
  <div class="stat" style="left:980px"><div class="stat-num">850+</div><div class="stat-label">Happy Owners</div></div>
</section>

<section class="section properties">
  <h2 class="abs heading center" style="top:66px;width:100%">AVAILABLE <b>PROPERTIES</b></h2>
  <div class="underline" style="left:556px;top:116px;width:90px"></div>
  <div class="arrow-btn" style="left:67px;border:1px solid #333">
    <svg width="14" height="10" viewBox="0 0 14 10"><path d="M13 5H1M5 1L1 5l4 4" fill="none" stroke="#333" stroke-width="1.4"/></svg>
  </div>
  <div class="arrow-btn" style="left:1094px;background:var(--green)">
    <svg width="14" height="10" viewBox="0 0 14 10"><path d="M1 5h12M9 1l4 4-4 4" fill="none" stroke="#fff" stroke-width="1.4"/></svg>
  </div>
  <article class="prop-card" style="left:141px">
    <div class="prop-photo" role="img" aria-label="White modern apartment facade" style="background:linear-gradient(180deg,#c9d3dc,#e9e9e6 60%,#8d8f90)"></div>
    <div class="prop-count">12 Property</div><div class="prop-name">Sunset Street</div>
  </article>
  <article class="prop-card" style="left:374px">
    <div class="prop-photo" role="img" aria-label="Dark modern house lit at dusk" style="background:linear-gradient(180deg,#6b88a8,#3a4454 55%,#8a6a3d)"></div>
    <div class="prop-count">34 Property</div><div class="prop-name">Union Avenue</div>
  </article>
  <article class="prop-card" style="left:607px">
    <div class="prop-photo" role="img" aria-label="Modern house with pool and wooden slats" style="background:linear-gradient(180deg,#8fb6d8,#b7a88d 55%,#6d6a55)"></div>
    <div class="prop-count">56 Property</div><div class="prop-name">Washington Street</div>
  </article>
  <article class="prop-card" style="left:840px">
    <div class="prop-photo" role="img" aria-label="Brick and grey modern building" style="background:linear-gradient(90deg,#a24f36,#6b6e72 60%,#c5ccd3)"></div>
    <div class="prop-count">78 Property</div><div class="prop-name">Oak Boulevard</div>
  </article>
  <a class="btn btn-solid" style="left:533px;top:471px;width:134px;height:38px">VIEW MORE
    <svg width="14" height="10" viewBox="0 0 14 10"><path d="M1 5h12M9 1l4 4-4 4" fill="none" stroke="#1f3d17" stroke-width="1.4"/></svg></a>
</section>

<section class="section about">
  <div class="abs about-photo" role="img" aria-label="Contemporary two-storey villa at evening"></div>
  <div class="abs badge"><div class="badge-num">25+</div><div class="badge-label">YEARS OF EXPERIENCE</div></div>
  <p class="abs eyebrow">ABOUT</p>
  <h2 class="abs about-title">KEYSTONE <b>MORTGAGE</b><br><b>AND FINANCE</b></h2>
  <p class="abs about-text">Keystone Mortgage Originates Residential Home loans in Florida and Commercial and business financing in all 50 States. We have over 25 years of experience in ALL types of real estate and commercial lending. We are strategically partnered to help you obtain ALL necessary components of residential and commercial lending. From the RIGHT lending partners to the best practice Insurance avenues and commercial and residential real estate partners</p>
  <a class="btn btn-solid" style="left:639px;top:417px;width:135px;height:41px">READ MORE
    <svg width="14" height="10" viewBox="0 0 14 10"><path d="M1 5h12M9 1l4 4-4 4" fill="none" stroke="#1f3d17" stroke-width="1.4"/></svg></a>
  <div class="abs call">
    <div class="call-icon"><svg width="18" height="18" viewBox="0 0 24 24"><path d="M6.6 10.8a15 15 0 006.6 6.6l2.2-2.2c.3-.3.7-.4 1-.2 1.1.4 2.3.6 3.6.6.6 0 1 .4 1 1V20c0 .6-.4 1-1 1A17 17 0 013 4c0-.6.4-1 1-1h3.5c.6 0 1 .4 1 1 0 1.3.2 2.5.6 3.6.1.3 0 .7-.2 1z" fill="var(--green)"/></svg></div>
    <div><small>CALL US</small><strong>+1 (555) 204-3318</strong></div>
  </div>
</section>

<section class="section services">
  <div class="services-photo" role="img" aria-label="Waterfront city skyline with a Ferris wheel"></div>
  <h2 class="abs heading center" style="top:150px;width:100%">OUR <b>SERVICES</b></h2>
  <article class="service-card" style="left:141px">
    <div class="service-icon"><svg width="40" height="40" viewBox="0 0 40 40" fill="none" stroke="#fff" stroke-width="2"><rect x="8" y="10" width="24" height="26"/><path d="M4 36h32M14 16h4M22 16h4M14 22h4M22 22h4M17 36v-7h6v7M12 10l8-6 8 6"/></svg></div>
    <h3 class="service-title">Commercial Loans</h3>
    <p class="service-text">Lorem Ipsum is simply dummy text of the printing and typesetting industry. Lorem Ipsum has been</p>
    <a class="btn btn-outline">READ MORE <svg width="14" height="10" viewBox="0 0 14 10"><path d="M1 5h12M9 1l4 4-4 4" fill="none" stroke="#333" stroke-width="1.4"/></svg></a>
  </article>
  <article class="service-card" style="left:456px">
    <div class="service-icon"><svg width="40" height="40" viewBox="0 0 40 40" fill="none" stroke="#fff" stroke-width="2.4"><path d="M4 20L20 6l16 14M9 16v18h22V16"/><rect x="16" y="22" width="8" height="8"/></svg></div>
    <h3 class="service-title">Residential Loans</h3>
    <p class="service-text">Lorem Ipsum is simply dummy text of the printing and typesetting industry. Lorem Ipsum has been</p>
    <a class="btn btn-outline">READ MORE <svg width="14" height="10" viewBox="0 0 14 10"><path d="M1 5h12M9 1l4 4-4 4" fill="none" stroke="#333" stroke-width="1.4"/></svg></a>
  </article>
  <article class="service-card" style="left:770px">
    <div class="service-icon"><svg width="40" height="40" viewBox="0 0 40 40" fill="none" stroke="#fff" stroke-width="2.4"><path d="M3 20L16 8l9 8M7 17v17h12"/><path d="M34 8L20 34"/><text x="24" y="34" font-size="16" fill="#fff" stroke="none" font-family="Outfit,sans-serif" font-weight="700">$</text></svg></div>
    <h3 class="service-title">Property Mortgage</h3>
    <p class="service-text">Lorem Ipsum is simply dummy text of the printing and typesetting industry. Lorem Ipsum has been</p>
    <a class="btn btn-outline">READ MORE <svg width="14" height="10" viewBox="0 0 14 10"><path d="M1 5h12M9 1l4 4-4 4" fill="none" stroke="#333" stroke-width="1.4"/></svg></a>
  </article>
</section>

<section class="section rates">
  <h2 class="abs heading center" style="top:48px;width:100%;line-height:44px">STAY INFORMED<br><b>ABOUT MORTGAGE RATES</b></h2>
  <p class="abs rates-text center">Mortgage rates fluctuate based on various factors such as loan type, market conditions, and your personal financial profile. Rates may change frequently, and it's important to get the most accurate and up-to-date information for your unique situation.</p>
  <div class="abs chart-card">
    <div class="chart-title">Last 90 Days of 30-Year Mortgage Rate Average</div>
    <div class="chart-sub">Average of nationwide rates for 30-year fixed-rate new purchase loans with at least a 20% down payment and an applicant credit score of 680 to 739.</div>
    <svg width="542" height="413" viewBox="0 0 542 413" font-family="Outfit,sans-serif">
      <g stroke="#e2e2e2" stroke-width="1">
        <path d="M64 86.4H522M64 115.8H522M64 145.2H522M64 174.6H522M64 204H522M64 233.4H522M64 262.8H522M64 292.2H522M64 321.6H522M64 351H522"/>
        <path d="M64 86V351M102.2 86V351M140.4 86V351M178.5 86V351M216.7 86V351M254.9 86V351M293.1 86V351M331.3 86V351M369.4 86V351M407.6 86V351M445.8 86V351M484 86V351M522 86V351"/>
      </g>
      <g font-size="9" fill="#333" text-anchor="end">
        <text x="28" y="89">7.8%</text><text x="28" y="118">7.6</text><text x="28" y="148">7.4</text><text x="28" y="177">7.2</text><text x="28" y="207">7.0</text><text x="28" y="236">6.8</text><text x="28" y="265">6.6</text><text x="28" y="295">6.4</text><text x="28" y="324">6.2</text><text x="28" y="354">6.0</text>
      </g>
      <g font-size="9" fill="#333" text-anchor="middle">
        <text x="64" y="370">2/19</text><text x="102" y="370">2/26</text><text x="140" y="370">3/4</text><text x="178" y="370">3/11</text><text x="217" y="370">3/18</text><text x="255" y="370">3/25</text><text x="293" y="370">4/1</text><text x="331" y="370">4/8</text><text x="369" y="370">4/15</text><text x="408" y="370">4/22</text><text x="446" y="370">4/29</text><text x="484" y="370">5/6</text><text x="522" y="370">5/13</text>
      </g>
      <polyline fill="none" stroke="var(--chart)" stroke-width="2" stroke-linejoin="round" points="64,206.7 69.5,211.2 80.4,196.4 91.3,211.2 102.2,215.6 113.1,225.9 124,218.5 134.9,230.3 145.8,236.2 156.7,247.9 162.1,258.3 167.6,253.8 178.5,245 189.4,233.2 200.3,225.9 205.8,211.2 211.2,218.5 222.1,225.9 233,239.1 243.9,245 254.8,247.9 260.3,253.8 265.7,247.9 276.6,240.6 287.5,230.3 298.4,218.5 309.3,211.2 320.2,196.4 331.1,203.8 342.1,189.1 353,181.7 363.9,192 374.8,174.4 385.7,162.6 396.6,171.4 407.5,159.6 418.4,149.3 429.3,162.6 440.2,171.4 451.1,189.1 462,186.1 472.9,195 483.8,192 494.7,200.8 505.6,203.8 522,196.4"/>
      <g fill="#fff" stroke="#555" stroke-width="1.2">
        <circle cx="80.4" cy="196.4" r="3"/><circle cx="205.8" cy="211.2" r="3"/><circle cx="162.1" cy="258.3" r="3"/><circle cx="260.3" cy="253.8" r="3"/><circle cx="418.4" cy="149.3" r="3"/><circle cx="522" cy="196.4" r="3"/>
      </g>
      <g font-size="9" font-weight="600" fill="#2d3f6b" text-anchor="middle">
        <text x="80" y="170">7.05%</text><text x="80" y="181">Feb 22</text>
        <text x="205" y="184">6.95%</text><text x="205" y="195">Mar 16-17</text>
        <text x="162" y="277">6.63%</text><text x="162" y="288">Mar 8-10</text>
        <text x="260" y="272">6.66%</text><text x="260" y="283">Mar 27</text>
        <text x="418" y="121">7.37%</text><text x="418" y="132">Apr 25</text>
        <text x="505" y="218">7.05%</text><text x="505" y="229">May 13</text>
      </g>
      <circle cx="464" cy="392" r="4" fill="var(--green-dark)"/>
      <text x="472" y="395" font-size="6" fill="var(--green-dark)">Keystone Lending</text>
    </svg>
  </div>
  <a class="btn btn-solid" style="left:541px;top:729px;width:118px;height:38px">SIGN UP
    <svg width="14" height="10" viewBox="0 0 14 10"><path d="M1 5h12M9 1l4 4-4 4" fill="none" stroke="#1f3d17" stroke-width="1.4"/></svg></a>
</section>

<section class="section testimonials">
  <h2 class="abs heading center" style="top:70px;width:100%">WHAT OUR <b>CLIENTS SAY</b></h2>
  <div class="underline" style="left:586px;top:116px;width:224px;height:3px"></div>
  <article class="t-card" style="left:-329px">
    <div class="quote">”</div>
    <p class="t-text">Lorem Ipsum Is Simply Dummy Text Of The Printintypesetting Industry. Lorem Ipsum Has Been The Industry's Standdummy Text Ever Since The 1500s, When An Unknown Printer Togalley Of Type And Scrambled It To Make A Type Specimen Book. It</p>
  </article>
  <article class="t-card" style="left:141px">
    <div class="avatar" role="img" aria-label="Client portrait"></div>
    <div class="t-name">Marcus Bellamy</div><div class="stars">★★★★★</div>
    <div class="quote">”</div>
    <p class="t-text">Lorem Ipsum Is Simply Dummy Text Of The Printintypesetting Industry. Lorem Ipsum Has Been The Industry's Standdummy Text Ever Since The 1500s, When An Unknown Printer Togalley Of Type And Scrambled It To Make A Type Specimen Book. It Has Survived Not Only Five Centuries</p>
  </article>
  <article class="t-card" style="left:624px">
    <div class="avatar" role="img" aria-label="Client portrait"></div>
    <div class="t-name">Lena Korvath</div><div class="stars">★★★★★</div>
    <div class="quote">”</div>
    <p class="t-text">Lorem Ipsum Is Simply Dummy Text Of The Printintypesetting Industry. Lorem Ipsum Has Been The Industry's Standdummy Text Ever Since The 1500s, When An Unknown Printer Togalley Of Type And Scrambled It To Make A Type Specimen Book. It Has Survived Not Only Five Centuries</p>
  </article>
  <article class="t-card" style="left:1093px">
    <div class="avatar" role="img" aria-label="Client portrait"></div>
    <p class="t-text">Lorem Ipsum Is Simply Dummy Text Of The Printintypesetting Industry. Lorem Ipsum Has Been The Industry's Standdummy Text Ever Since The 1500s, When An Unknown Printer Togalley Of Type And Scrambled It To Make A Type Specimen Book. It Has Survived</p>
  </article>
  <div class="dots"><i></i><i></i><i class="on"></i><i></i><i></i><i></i></div>
</section>

<section class="section contact">
  <h2 class="abs heading center" style="top:74px;width:100%">GET IN <b>TOUCH</b></h2>
  <p class="abs contact-sub center">Please Send Me A Message For General Inquiries Or Reservations.</p>
  <div class="field" style="left:291px;top:197px;width:301px;height:51px">
    <svg width="13" height="13" viewBox="0 0 14 14" fill="none" stroke="#aaa" stroke-width="1.2"><circle cx="7" cy="4.5" r="3"/><path d="M1.5 13c.5-3 2.7-4.5 5.5-4.5s5 1.5 5.5 4.5"/></svg><span class="sep"></span>First Name</div>
  <div class="field" style="left:605px;top:197px;width:304px;height:51px">
    <svg width="13" height="13" viewBox="0 0 14 14" fill="none" stroke="#aaa" stroke-width="1.2"><circle cx="7" cy="4.5" r="3"/><path d="M1.5 13c.5-3 2.7-4.5 5.5-4.5s5 1.5 5.5 4.5"/></svg><span class="sep"></span>Last Name</div>
  <div class="field" style="left:291px;top:263px;width:301px;height:53px">
    <svg width="14" height="12" viewBox="0 0 14 12" fill="none" stroke="#aaa" stroke-width="1.2"><rect x="1" y="1.5" width="12" height="9" rx="1"/><path d="M1 2l6 5 6-5"/></svg><span class="sep"></span>Your Email</div>
  <div class="field" style="left:605px;top:263px;width:304px;height:53px">
    <svg width="13" height="13" viewBox="0 0 24 24" fill="none" stroke="#aaa" stroke-width="2"><path d="M6.6 10.8a15 15 0 006.6 6.6l2.2-2.2 4.6 1.4V20A17 17 0 013 4h3.5l1.4 4.6z"/></svg><span class="sep"></span>Phone</div>
  <div class="field" style="left:291px;top:331px;width:618px;height:107px">
    <svg width="13" height="13" viewBox="0 0 14 14" fill="none" stroke="#aaa" stroke-width="1.2"><path d="M2 2h10v7H6l-3 3V9H2z"/></svg><span class="sep"></span>Your Message</div>
  <div class="abs send">Send Message</div>
</section>

<footer class="section site-footer">
  <div class="abs footer-brand"><span class="brand-mark"></span><span class="brand-name">Keystone Lending and Capital of Florida</span></div>
  <p class="abs footer-note">Latest Updates, Exclusive Content, And Special Offers? Subscribe To Our Newsletter!</p>
  <div class="abs newsletter">
    <svg width="12" height="10" viewBox="0 0 14 12" fill="none" stroke="#aaa" stroke-width="1.2"><rect x="1" y="1.5" width="12" height="9" rx="1"/><path d="M1 2l6 5 6-5"/></svg>Your Email
    <span class="go"><svg width="12" height="10" viewBox="0 0 14 10"><path d="M1 5h12M9 1l4 4-4 4" fill="none" stroke="#fff" stroke-width="1.6"/></svg></span>
  </div>

  <div class="abs" style="left:481px;top:62px">
    <h4 class="f-head">Quick Links</h4>
    <ul class="f-list" style="margin-top:14px"><li>Home</li><li>About Us</li><li>Properties</li><li>Contact Us</li></ul>
  </div>

  <h4 class="abs f-head" style="left:635px;top:62px">Contact Details</h4>
  <div class="detail" style="top:100px">
    <svg width="12" height="14" viewBox="0 0 12 14"><path d="M6 0a5 5 0 015 5c0 3.5-5 9-5 9S1 8.5 1 5a5 5 0 015-5z" fill="#fff"/><circle cx="6" cy="5" r="2" fill="var(--footer)"/></svg>
    <span>77 Harbor Mill Lane, Suite 4,</span><span>Bay Point, FL USA</span>
  </div>
  <div class="detail" style="top:150px">
    <svg width="12" height="12" viewBox="0 0 24 24"><path d="M6.6 10.8a15 15 0 006.6 6.6l2.2-2.2 4.6 1.4V21A17 17 0 013 4h4.5l1.4 4.6z" fill="#fff"/></svg>
    <span>Phone</span><span>+1 555 302 7741</span>
  </div>
  <div class="detail" style="top:200px">
    <svg width="12" height="10" viewBox="0 0 14 12"><rect x="1" y="1.5" width="12" height="9" fill="#fff"/><path d="M1 2l6 5 6-5" fill="none" stroke="var(--footer)" stroke-width="1.2"/></svg>
    <span>Email</span><span style="font-size:11px">info@keystonelendingandcapital.example</span>
  </div>

  <h4 class="abs f-head" style="left:939px;top:62px">Social Media</h4>
  <div class="social" style="top:100px"><i class="on"></i>Social Feed</div>
  <div class="social" style="top:141px"><i></i>Video Channel</div>
  <div class="social" style="top:182px"><i></i>Pro Network</div>
  <div class="social" style="top:223px"><i></i>Photo Stream</div>

  <div class="abs f-rule"></div>
  <p class="abs copyright center">© 2025 Keystone Lending and Capital. All Rights Reserved.</p>
</footer>

</body>
</html>
```